Chauffeur Car Driver Needing a design with/without logo for business cards

I'm a chauffeur car driver in Melbourne Australia. I have an extensive list of personal customers and need to provide a professional business card to new customers.
My business name is 'RivaPlus'.
I offer a personalised service to customer who need a transport alternative to taxis. I don't want it to look too 'upmarket' as i don't want it to seem too expensive or only for special occasions. The majority of my clients are business professionals who use me for airport transfers.
I definitely don't want the card/logo to have an image of a car/road etc. I prefer something abstract. A 'pencil-line'-type font will grab my attention but not absolutely necessary. Not too 'digital' or 'ultra - modern' looking.
I need the card to display the following information
Riva Plus - main logo/text
Chauffeur Cars - sub text
Marco Devilles
0452 918 306
bookings@RivaPlus.example.au
I would like the focus to be on 'RivaPlus' with everything else smaller.
Look forward to seeing ideas!!!!
Target Market(s)
Business Corporate Professionals
Industry/Entity Type
Airport
Requirements
Nice to have
- Pencil line type font
Should not have
- Images of cars, road, tyres, steering wheel etc.

```html
<!DOCTYPE html>
<html lang="en">
<head>
<meta charset="utf-8">
<title>RivaPlus Chauffeur Cars – Business Card</title>
<link rel="stylesheet" href="https://fonts.googleapis.com/css2?family=Arimo:wght@400;700&family=PT+Sans+Narrow:wght@400;700&display=swap">
<style>
  :root {
    --page-bg: #ffffff;
    --band-slate: #7f9aa8;
    --card-white: #ffffff;
    --ink: #111111;
    --band-black: #000000;
    --name-slate: #7f9aa8;
    --card-shadow: rgba(0, 0, 0, 0.28);
  }
  * { margin: 0; padding: 0; box-sizing: border-box; }
  html, body {
    width: 1200px;
    height: 800px;
    overflow: hidden;
    background: var(--page-bg);
  }
  .canvas {
    position: relative;
    width: 1200px;
    height: 800px;
  }
  .business-card {
    position: absolute;
    left: 150px;
    top: 130px;
    width: 900px;
    height: 540px;
    background: var(--card-white);
    box-shadow: 0 4px 14px var(--card-shadow);
    overflow: hidden;
  }
  .brand-band {
    position: absolute;
    left: 0; top: 0;
    width: 100%;
    height: 232px;
    background: var(--band-slate);
  }
  .brand-lockup {
    position: absolute;
    left: 262px;
    top: 82px;
    font-family: "Arimo", Arial, sans-serif;
    color: var(--ink);
  }
  .brand-name {
    font-weight: 700;
    font-size: 74px;
    line-height: 1;
    letter-spacing: -3px;
    text-transform: uppercase;
  }
  .brand-tagline {
    font-weight: 400;
    font-size: 31px;
    line-height: 1;
    margin-top: 4px;
    padding-left: 70px;
  }
  .contact-block {
    position: absolute;
    left: 462px;
    top: 286px;
    font-family: "PT Sans Narrow", "Arial Narrow", sans-serif;
    font-size: 27px;
    line-height: 34px;
    color: var(--ink);
  }
  .contact-name {
    font-weight: 700;
    color: var(--name-slate);
  }
  .footer-band {
    position: absolute;
    left: 0; bottom: 0;
    width: 100%;
    height: 84px;
    background: var(--band-black);
  }
</style>
</head>
<body>
  <main class="canvas">
    <article class="business-card">
      <header class="brand-band">
        <div class="brand-lockup">
          <div class="brand-name">RivaPlus</div>
          <div class="brand-tagline">Chauffeur Cars</div>
        </div>
      </header>
      <section class="contact-block">
        <p class="contact-name">Marco Devilles</p>
        <p class="contact-phone">0452 918 306</p>
        <p class="contact-email">bookings@RivaPlus.example.au</p>
      </section>
      <footer class="footer-band"></footer>
    </article>
  </main>
</body>
</html>
```